Begegnungskonzert Kammerchor Lumivessa Berlin und Tonbrückener Kinderchor Peking
Zielgruppe
Es geht um ein Konzertplakat für den Kammerchor Lumivessa Berlin. www.lumivessa-chor.example
Wir haben ein Begegnungskonzert mit einem Chinesischen Kinderchor, der Berlin besucht.
Aufgabenstellung
Kammerchor Lumivessa Berlin, Leitung: Karsten Brodt
Tonbrückener Kinderchor Peking, Leitung: Prof. Zhou Wen
21.08.2017, 19:00 Uhr Quellkapelle Berlin Wilmersdorf, Falkenauer Str. 27, 14183 Berlin
Eintritt frei, Spenden erbeten
Werke von Albrechtsen, Caspo, Thornvik, Pemberley und vielen mehr...
Logos und Farben bitte von unserer Website übernehmen!

```html
<!DOCTYPE html>
<html lang="de">
<head>
<meta charset="utf-8">
<title>Begegnungskonzert Berlin // Peking</title>
<link rel="stylesheet" href="https://fonts.googleapis.com/css2?family=Roboto:wght@300;400;500;700&display=swap">
<style>
  :root {
    --backdrop: #e6e6e4;
    --paper: #ffffff;
    --ink: #1d1d1d;
    --ink-soft: #3a3a3a;
    --triangle: #1e1e1e;
    --photo-warm-a: #6b4a2c;
    --photo-warm-b: #c79a68;
    --photo-light-a: #f6d9bf;
    --photo-light-b: #e9b68f;
  }
  html, body {
    margin: 0;
    width: 1200px;
    height: 928px;
    overflow: hidden;
    background: var(--backdrop);
    font-family: "Roboto", Arial, sans-serif;
    color: var(--ink);
  }
  .poster {
    position: absolute;
    left: 294px;
    top: 24px;
    width: 612px;
    height: 880px;
    background: var(--paper);
    overflow: hidden;
    box-shadow: 0 4px 18px rgba(0,0,0,0.18);
  }
  .poster__shapes {
    position: absolute;
    inset: 0;
    width: 100%;
    height: 100%;
  }
  .poster__url {
    position: absolute;
    left: 37px;
    top: 38px;
    font-size: 10px;
    font-weight: 400;
    color: var(--ink-soft);
  }
  .choirs {
    position: absolute;
    right: 37px;
    top: 34px;
    text-align: right;
  }
  .choir { margin-bottom: 12px; }
  .choir__name { font-size: 14.5px; font-weight: 500; letter-spacing: 0.2px; line-height: 18px; }
  .choir__city { font-size: 10px; font-weight: 700; line-height: 14px; }
  .choir__lead { font-size: 10px; font-weight: 300; line-height: 15px; color: var(--ink-soft); }
  .brand-name {
    position: absolute;
    left: 37px;
    top: 112px;
    width: 90px;
    font-size: 14px;
    font-weight: 400;
    line-height: 16px;
    color: #ffffff;
  }
  .headline {
    position: absolute;
    left: 37px;
    top: 446px;
    margin: 0;
    font-size: 40px;
    font-weight: 700;
    line-height: 45px;
    letter-spacing: 0.3px;
    color: var(--ink);
  }
  .event-info {
    position: absolute;
    left: 37px;
    top: 778px;
    line-height: 16px;
  }
  .event-info__date { font-size: 14.5px; font-weight: 500; line-height: 18px; }
  .event-info__entry { font-size: 10px; font-weight: 700; }
  .event-info__place { font-size: 10.5px; font-weight: 300; color: var(--ink-soft); }
  .program {
    position: absolute;
    right: 37px;
    top: 780px;
    text-align: right;
  }
  .program__intro { font-size: 10.5px; font-weight: 300; line-height: 14px; color: var(--ink-soft); }
  .program__composers { font-size: 14.5px; font-weight: 500; line-height: 18px; }
  .program__more { font-size: 10px; font-weight: 700; line-height: 15px; }
</style>
</head>
<body>
  <article class="poster">
    <svg class="poster__shapes" viewBox="0 0 574 826" preserveAspectRatio="none">
      <defs>
        <linearGradient id="warmPhoto" x1="0" y1="0" x2="1" y2="1">
          <stop offset="0" stop-color="var(--photo-warm-b)"/>
          <stop offset="0.55" stop-color="var(--photo-warm-a)"/>
          <stop offset="1" stop-color="#2a2630"/>
        </linearGradient>
        <linearGradient id="lightPhoto" x1="0" y1="0" x2="0" y2="1">
          <stop offset="0" stop-color="var(--photo-light-b)"/>
          <stop offset="1" stop-color="var(--photo-light-a)"/>
        </linearGradient>
      </defs>
      <polygon class="photo photo--children" role="img" aria-label="Foto: Dirigent probt mit dem Kinderchor in Uniform"
               points="0,194 244,119 574,218 574,484 0,372" fill="url(#warmPhoto)"/>
      <polygon class="triangle triangle--top" points="0,42 244,119 0,194" fill="var(--triangle)"/>
      <polygon class="triangle triangle--white" points="0,372 474,484 0,644" fill="var(--paper)"/>
      <polygon class="photo photo--chamber-choir" role="img" aria-label="Foto: Kammerchor singt im Konzertsaal vor dem Dirigenten"
               points="0,644 574,534 574,826 0,826" fill="url(#lightPhoto)"/>
      <polygon class="triangle triangle--right" points="574,469 364,540 574,594" fill="var(--triangle)"/>
    </svg>

    <div class="poster__url">www.lumivessa-chor.example</div>

    <div class="brand-name">Lumivessa Berlin</div>

    <div class="choirs">
      <div class="choir">
        <div class="choir__name">KAMMERCHOR LUMIVESSA</div>
        <div class="choir__city">BERLIN</div>
        <div class="choir__lead">Leitung: Karsten Brodt</div>
      </div>
      <div class="choir">
        <div class="choir__name">TONBRÜCKENER KINDERCHOR</div>
        <div class="choir__city">PEKING</div>
        <div class="choir__lead">Leitung: Prof. Zhou Wen</div>
      </div>
    </div>

    <h1 class="headline">BEGEGNUNGS-<br>KONZERT<br>BERLIN//PEKING</h1>

    <div class="event-info">
      <div class="event-info__date">21.08.2017 // 19 UHR</div>
      <div class="event-info__entry">EINTRITT FREI // SPENDEN ERBETEN</div>
      <div class="event-info__place">Quellkapelle Berlin-Wilmersdorf</div>
      <div class="event-info__place">Falkenauer Str. 27 // 14183 Berlin</div>
    </div>

    <div class="program">
      <div class="program__intro">Werke von</div>
      <div class="program__composers">ALBRECHTSEN,</div>
      <div class="program__composers">CASPO, THORNVIK, PEMBERLEY</div>
      <div class="program__more">UND VIELEN MEHR</div>
    </div>
  </article>
</body>
</html>
```